Software Company Requires Website

We need a web design for a new mobile software development company based in London named Velmark Solutions.
The design needs to be clean and smooth. Not too flashy, not too boring.
I would like to try the design with some warm colors, and maybe a headline or something highlighted with a strong color. ( logo ? ) The layout should be something like the bellow links, all in one page.

http://quorbit.example/
http://www.telvane.example/
http://www.work-plover.example/
http://www.brisk.example/
http://www.fenlowtech.example/us/

Now some of them they seem different from the others, but in each of them there is something that ticks my brain, so it`s up to you to surprise me.

I have uploaded the logo of the company, so you guys can fit that in your design as well.
Updates

Hy everybody This will be the last update for the brief. The company will focus in the beginning for mobile development only, so i would like the website design to be done in a matter that will reflect that. We will develop IOS, Android and Windows applications. We will also require 3 pages: One for the home menu, one for portfolio and one for contact us. The layout should be the same ( one page scroll down ) but the design of the 3 pages different. Please readdress the brief. Hope that i provided enough information for the scope of the project.

I have uploaded the logo that you guys can use. If the logo requires small modifications you can adjust that to suit your idea as long as the logo does not change completely.

Target Market(s)

High End companies that require simplified software solutions.

Industry/Entity Type

It Company

Number of Pages Required

3 page

Requirements
Must have
• One page scroll down layout for 3 pages:
• one for home page, one for portfolio and one for contact us.
• In the portfolio page we would like to have different display options for given examples of applications ( min 3 )

```html
<!DOCTYPE html>
<html lang="en">
<head>
<meta charset="utf-8">
<title>Velmark Solutions</title>
<link href="https://fonts.googleapis.com/css2?family=Roboto:wght@300;400;500;700&display=swap" rel="stylesheet">
<style>
:root{
  --blue:#1f74c0;
  --white:#ffffff;
  --ink:#555555;
  --ink-soft:#8a8a8a;
  --line:#d9d9d9;
  --grey-bg:#f2f2f2;
  --dark:#141414;
  --darker:#0b0b0b;
  --panel:#262626;
  --field:#474747;
  --accent:#f5a300;
  --red:#e53935;
  --social:#1d8fd8;
}
*{box-sizing:border-box;margin:0;padding:0}
html,body{width:1200px;height:2190px;overflow:hidden}
body{font-family:'Roboto',Arial,sans-serif;color:var(--ink);background:var(--white)}
section,header,footer{position:relative;width:1200px}
.abs{position:absolute}
.center{left:0;right:0;text-align:center}

/* header */
.hero{height:328px;background:var(--blue);color:var(--white)}
.brand{left:282px;top:18px;display:flex;align-items:center;gap:9px;font-size:21px;font-weight:500;color:var(--white);white-space:nowrap}
.brand-mark{width:16px;height:16px;border:2px solid var(--white)}
.nav-link{top:28px;font-size:10px;font-weight:500;white-space:nowrap}
.nav-cta{left:828px;top:23px;width:78px;height:24px;background:var(--white);color:var(--blue);font-size:10px;font-weight:500;display:flex;align-items:center;justify-content:center}
.hero-title{top:174px;font-size:30px;font-weight:500}
.hero-sub{top:216px;font-size:12px;font-weight:300}

/* services */
.services{height:246px}
.section-title{font-size:14px;font-weight:500;letter-spacing:.5px;color:#444}
.section-sub{font-size:10px;color:var(--ink-soft)}
.service{width:170px;text-align:center;top:82px}
.service h3{font-size:10px;font-weight:500;color:#555;margin-top:10px;letter-spacing:.4px}
.service p{font-size:8.5px;line-height:12px;color:var(--ink-soft);margin-top:10px}

/* works band */
.works{height:153px;background:linear-gradient(100deg,#3f7ab3 0%,#2d6aa6 45%,#24609d 100%);color:var(--white)}
.works h2{top:50px;font-size:20px;font-weight:400}
.works p{top:82px;font-size:10px;color:#d6e6f5}

/* portfolio */
.portfolio{height:385px}
.device{left:322px;top:160px;width:269px;height:131px;background:linear-gradient(160deg,#e8e8e8,#bfc3c8 55%,#f3f3f3);border-radius:8px}
.showcase-text{left:615px;top:158px;width:255px}
.showcase-text h3{font-size:14px;font-weight:400;color:#666}
.showcase-text p{font-size:8.5px;line-height:12px;color:var(--ink-soft);margin-top:12px}
.pager{top:345px;display:flex;justify-content:center;gap:4px}
.pager span{width:9px;height:9px;border-radius:50%;border:1px solid var(--red)}
.pager span.on{background:var(--red)}

/* team */
.team{height:377px;background:var(--grey-bg)}
.member{width:150px;text-align:center;top:122px}
.member h4{font-size:10px;font-weight:500;color:#333}
.member .role{font-size:8px;color:#666;margin-top:8px}
.avatar{width:72px;height:72px;border-radius:50%;margin:10px auto 0;background:radial-gradient(circle,#8c7a6c,#3e3530);border:2px solid var(--white)}
.socials{display:flex;gap:5px;justify-content:center;margin-top:14px}
.socials span{width:14px;height:14px;border-radius:50%;background:var(--social)}
.member p{font-size:7.5px;line-height:11px;color:#777;margin:8px auto 0;width:112px}

/* about */
.about{height:263px}
.about-lead{top:118px;width:440px;left:380px;font-size:7.5px;line-height:11px;font-weight:500;color:#333;text-align:center;text-transform:uppercase}
.about-body{top:168px;width:440px;left:380px;font-size:7.5px;line-height:11px;color:#777;text-align:center}
.read-more{top:212px;font-size:7px;color:#555;text-decoration:underline}

/* contact */
.contact{height:394px;background:var(--dark);color:#bbb}
.contact .section-title{color:#ddd}
.contact-info{left:328px;top:116px;font-size:8.5px;line-height:18px;color:#aaa}
.contact-info h4{font-size:11px;font-weight:400;color:#888;margin-bottom:8px}
.contact-info b{font-weight:500;color:#ddd}
.contact-info a{color:#3ea0e8;text-decoration:none}
.enquiry{left:611px;top:114px;width:237px;height:254px;background:var(--panel);padding:16px 18px}
.enquiry h4{font-size:9px;font-weight:500;color:#ddd;margin-bottom:12px}
.field{height:26px;background:var(--field);margin:0 0 8px 0;font-size:8px;color:#bbb;padding:8px 10px}
.field.big{height:72px}
.send{position:absolute;right:22px;bottom:18px;width:76px;height:26px;background:var(--accent);color:#222;font-size:8px;font-weight:700;display:flex;align-items:center;justify-content:center}

footer{height:44px;background:var(--darker);color:#888;font-size:8px;display:flex;align-items:center;justify-content:center}
</style>
</head>
<body>

<header class="hero">
  <div class="abs brand"><span class="brand-mark"></span>Velmark Solutions</div>
  <nav>
    <span class="abs nav-link" style="left:569px">HOME</span>
    <span class="abs nav-link" style="left:629px">SERVICES</span>
    <span class="abs nav-link" style="left:694px">PORTFOLIO</span>
    <span class="abs nav-link" style="left:760px">ABOUT US</span>
  </nav>
  <div class="abs nav-cta">CONTACT US</div>
  <svg class="abs" style="left:338px;top:146px" width="508" height="14" viewBox="0 0 508 14">
    <line x1="0" y1="7" x2="508" y2="7" stroke="#ffffff" stroke-opacity=".55" stroke-width="1"/>
    <circle cx="248" cy="7" r="4" fill="#fff"/><circle cx="260" cy="7" r="4" fill="#fff"/>
  </svg>
  <h1 class="abs center hero-title">Lorem Ipsum is simply dummy text</h1>
  <p class="abs center hero-sub">Mobile Software Development Company based in London</p>
</header>

<section class="services">
  <h2 class="abs center section-title" style="top:44px">SERVICES</h2>
  <div class="abs service" style="left:331px">
    <svg width="44" height="44" viewBox="0 0 44 44" fill="none" stroke="#9a9a9a" stroke-width="2">
      <circle cx="18" cy="24" r="8"/><circle cx="18" cy="24" r="3"/>
      <path d="M18 12v4M18 32v4M6 24h4M26 24h4M10 16l3 3M23 29l3 3M10 32l3-3M23 19l3-3"/>
      <circle cx="33" cy="12" r="5"/><circle cx="33" cy="12" r="1.5"/>
    </svg>
    <h3>TECHNOLOGY</h3>
    <p>Lorem Ipsum is simply dummy text of<br>the printing and typesetting industry.<br>Lorem Ipsum has been</p>
  </div>
  <div class="abs service" style="left:506px">
    <svg width="44" height="44" viewBox="0 0 44 44" fill="none" stroke="#9a9a9a" stroke-width="2">
      <circle cx="22" cy="22" r="17"/><path d="M22 12v10l7 5"/>
    </svg>
    <h3>MARKETING</h3>
    <p>Lorem Ipsum is simply dummy text of<br>the printing and typesetting industry.<br>Lorem Ipsum has been</p>
  </div>
  <div class="abs service" style="left:686px">
    <svg width="44" height="44" viewBox="0 0 44 44" fill="none" stroke="#9a9a9a" stroke-width="2">
      <path d="M8 36l18-18M26 18a7 7 0 1 1 8-10l-5 5 3 3 5-5a7 7 0 0 1-11 7"/>
      <path d="M10 8l5 5M12 14l4-4M36 36L24 24"/>
    </svg>
    <h3>QUALITY</h3>
    <p>Lorem Ipsum is simply dummy text of<br>the printing and typesetting industry.<br>Lorem Ipsum has been</p>
  </div>
</section>

<section class="works" role="img" aria-label="Desk scene with tablet, mouse and keyboard in blue tones">
  <h2 class="abs center">Our Greatest Works</h2>
  <p class="abs center">Lorem for awesome Imaginations</p>
</section>

<section class="portfolio">
  <h2 class="abs center section-title" style="top:54px">OUR PORTFOLIO</h2>
  <p class="abs center section-sub" style="top:76px">Our Awesome Works</p>
  <svg class="abs" style="left:338px;top:94px" width="508" height="14" viewBox="0 0 508 14">
    <line x1="0" y1="7" x2="508" y2="7" stroke="#d9d9d9"/>
    <circle cx="248" cy="7" r="4" fill="#bbb"/><circle cx="260" cy="7" r="4" fill="#bbb"/>
  </svg>
  <div class="abs device" role="img" aria-label="Tablet and smartphone showing a mobile app dashboard"></div>
  <div class="abs showcase-text">
    <h3>Mobile Solutions</h3>
    <p>Mobile apps help growing teams work on the move. Organizations now need a quick, steady switch to a mobile way of working.</p>
    <p>With the right kind of tailored support, mobile teams will be able to raise their output and reach.</p>
  </div>
  <div class="abs center pager"><span class="on"></span><span></span><span></span><span></span><span></span><span></span></div>
</section>

<section class="team">
  <h2 class="abs center section-title" style="top:46px">TEAM</h2>
  <p class="abs center section-sub" style="top:67px">Lorem Ipsum is simply dummy text</p>
  <svg class="abs" style="left:338px;top:83px" width="508" height="14" viewBox="0 0 508 14">
    <line x1="0" y1="7" x2="508" y2="7" stroke="#d9d9d9"/>
    <circle cx="248" cy="7" r="4" fill="#bbb"/><circle cx="260" cy="7" r="4" fill="#bbb"/>
  </svg>
  <div class="abs member" style="left:273px">
    <h4>MARA ELLISON</h4><div class="role">Team Manager</div>
    <div class="avatar" role="img" aria-label="Portrait photo of team member"></div>
    <div class="socials"><span></span><span></span><span></span></div>
    <p>Lorem Ipsum is simply dummy text of the printing and typesetting industry. Lorem Ipsum has been the industry's standard dummy text ever since</p>
  </div>
  <div class="abs member" style="left:426px">
    <h4>TOM HAVERLY</h4><div class="role">Team Manager</div>
    <div class="avatar" role="img" aria-label="Portrait photo of team member"></div>
    <div class="socials"><span></span><span></span><span></span></div>
    <p>Lorem Ipsum is simply dummy text of the printing and typesetting industry. Lorem Ipsum has been the industry's standard dummy text ever since</p>
  </div>
  <div class="abs member" style="left:582px">
    <h4>NINA BROOKE</h4><div class="role">Team Manager</div>
    <div class="avatar" role="img" aria-label="Portrait photo of team member"></div>
    <div class="socials"><span></span><span></span><span></span></div>
    <p>Lorem Ipsum is simply dummy text of the printing and typesetting industry. Lorem Ipsum has been the industry's standard dummy text ever since</p>
  </div>
  <div class="abs member" style="left:740px">
    <h4>MARA ELLISON</h4><div class="role">Team Manager</div>
    <div class="avatar" role="img" aria-label="Portrait photo of team member"></div>
    <div class="socials"><span></span><span></span><span></span></div>
    <p>Lorem Ipsum is simply dummy text of the printing and typesetting industry. Lorem Ipsum has been the industry's standard dummy text ever since</p>
  </div>
</section>

<section class="about">
  <h2 class="abs center section-title" style="top:39px">ABOUT US</h2>
  <p class="abs center section-sub" style="top:61px">Lorem Ipsum is simply dummy text</p>
  <svg class="abs" style="left:338px;top:77px" width="508" height="14" viewBox="0 0 508 14">
    <line x1="0" y1="7" x2="508" y2="7" stroke="#d9d9d9"/>
    <circle cx="248" cy="7" r="4" fill="#bbb"/><circle cx="260" cy="7" r="4" fill="#bbb"/>
  </svg>
  <p class="abs about-lead">Lorem Ipsum is simply dummy text of the printing and typesetting industry. Lorem Ipsum has been the industry's standard dummy text ever since the 1500s, when an unknown printer took a galley of type and scrambled it to make a type specimen book.</p>
  <p class="abs about-body">Lorem Ipsum is simply dummy text of the printing and typesetting industry. Lorem Ipsum has been the industry's standard dummy text ever since the 1500s, when an unknown printer took a galley of type and scrambled it to make a type specimen book.</p>
  <div class="abs center read-more">READ MORE</div>
</section>

<section class="contact">
  <h2 class="abs center section-title" style="top:46px">CONTACT US</h2>
  <p class="abs center section-sub" style="top:67px">Lorem Ipsum is simply dummy text</p>
  <svg class="abs" style="left:338px;top:85px" width="508" height="14" viewBox="0 0 508 14">
    <line x1="0" y1="7" x2="508" y2="7" stroke="#555"/>
    <circle cx="248" cy="7" r="4" fill="#ddd"/><circle cx="260" cy="7" r="4" fill="#ddd"/>
  </svg>
  <div class="abs contact-info">
    <h4>CONTACT INFO</h4>
    <div>12 Harbour Lane, London, UK</div>
    <div><b>Phone</b> : +44 20 0000 1111</div>
    <div><b>Fax</b> : +44 20 0000 1112</div>
    <div><b>Email</b> : <a>info@velmark.example</a></div>
    <div><b>Web</b> : <a>www.velmark.example</a></div>
  </div>
  <div class="abs enquiry">
    <h4>ENQUIRY FORM</h4>
    <div class="field">Your Name</div>
    <div class="field">Your Email</div>
    <div class="field big">Message</div>
    <div class="send">SEND EMAIL</div>
  </div>
</section>

<footer>Copyright © 2014 Velmark Solutions</footer>

</body>
</html>
```